Business Card for Mortuary

We need a business card design for our mortuary. We are not the "traditional" mortuary and specialize in simple cremations and burials. We use a two sided card.

Industry/Entity Type

Funeral Home

Contact Information for Business Card

One side we would like to have with the general information of the mortuary:
Address: 4127 E. Larkspur Ave, Sun City, AZ 85399
Phone: 623-555-0142
email: hello@willowbendmortuary.example
website: willowbendmortuary.example

On the other side would like to have the information of employee:
Name: Mark T. Ellis
Email: mark@willowbendmortuary.example
Title: Funeral Director
Text: 602-555-0187

Font styles to use
Serif
Sans Serif

Requirements
Should not have
• Do not put any gothic images or things like a hearse or tombstone.

```html
<!DOCTYPE html>
<html lang="en">
<head>
<meta charset="utf-8">
<title>Willowbend Mortuary – Business Card</title>
<link href="https://fonts.googleapis.com/css2?family=Montserrat:wght@400;500&display=swap" rel="stylesheet">
<style>
  :root{
    --backdrop:#151515;
    --card:#2a2a2a;
    --lime:#b6e23a;
    --green:#7cc242;
    --text:#f2f2f2;
    --muted:#d6d6d6;
    --soft:#8a8a8a;
  }
  *{margin:0;padding:0;box-sizing:border-box}
  html,body{width:1200px;height:900px;overflow:hidden;background:var(--backdrop)}
  .canvas{position:relative;width:1200px;height:900px}
  .card{
    position:absolute;left:250px;width:700px;height:400px;
    background:var(--card);
    border-bottom:7px solid var(--lime);
    font-family:"Montserrat",Arial,sans-serif;
  }
  .card--front{top:32px}
  .card--back{top:468px}

  .identity{position:absolute;display:flex;flex-direction:column;gap:10px}
  .brand{display:flex;align-items:center;gap:12px}
  .brand__dot{width:22px;height:22px;border-radius:50%;background:var(--green);flex:none}
  .brand__name{font-weight:500;white-space:nowrap}
  .tagline{font-size:14px;font-weight:400;letter-spacing:.3px}

  .card--front .identity{left:0;right:0;top:165px;align-items:center}
  .card--front .brand__name{font-size:32px;color:var(--soft)}
  .card--front .tagline{color:var(--muted);font-size:16px}

  .card--back .identity{left:40px;top:172px}
  .card--back .brand__dot{width:18px;height:18px}
  .card--back .brand__name{font-size:24px;color:var(--text)}
  .card--back .tagline{color:var(--green);padding-left:30px}

  .divider-vertical{position:absolute;left:395px;top:40px;width:1.5px;height:300px;background:var(--green)}

  .contact{position:absolute;left:420px;top:48px;width:270px;color:var(--text)}
  .contact__name{font-size:26px;font-weight:500;color:var(--green);letter-spacing:2px;text-transform:uppercase}
  .contact__title{font-size:15px;margin:4px 0 10px}
  .contact__row{display:flex;align-items:center;gap:8px;font-size:13px;margin-bottom:6px;white-space:nowrap}
  .contact__row svg{width:12px;height:12px;flex:none}
  .contact__rule{height:1.5px;background:var(--green);margin:14px 0 16px}
  .contact__address{font-size:15px;line-height:1.35;margin-bottom:8px}
</style>
</head>
<body>
<main class="canvas">

  <section class="card card--front" aria-label="Card front">
    <div class="identity">
      <div class="brand">
        <span class="brand__dot"></span>
        <span class="brand__name">Willowbend Mortuary</span>
      </div>
      <p class="tagline">Affordable Cremation and Burial</p>
    </div>
  </section>

  <section class="card card--back" aria-label="Card back">
    <div class="identity">
      <div class="brand">
        <span class="brand__dot"></span>
        <span class="brand__name">Willowbend Mortuary</span>
      </div>
      <p class="tagline">Affordable Cremation and Burial</p>
    </div>

    <div class="divider-vertical"></div>

    <div class="contact">
      <h1 class="contact__name">Mark T. Ellis</h1>
      <p class="contact__title">Funeral Director</p>
      <p class="contact__row">
        <svg viewBox="0 0 12 12"><path d="M3 1l2 2.5-1.2 1.2a6 6 0 0 0 3.5 3.5L8.5 7 11 9l-1.3 1.8C5.5 10.5 1.5 6.5 1.2 2.3z" fill="var(--green)"/></svg>
        602-555-0187
      </p>
      <p class="contact__row">
        <svg viewBox="0 0 12 12"><rect x="1" y="2.5" width="10" height="7" fill="none" stroke="var(--green)" stroke-width="1.2"/><path d="M1 2.5l5 4 5-4" fill="none" stroke="var(--green)" stroke-width="1.2"/></svg>
        mark@willowbendmortuary.example
      </p>
      <div class="contact__rule"></div>
      <p class="contact__address">4127 E. Larkspur Ave,<br>Sun City, AZ 85399</p>
      <p class="contact__row">
        <svg viewBox="0 0 12 12"><path d="M3 1l2 2.5-1.2 1.2a6 6 0 0 0 3.5 3.5L8.5 7 11 9l-1.3 1.8C5.5 10.5 1.5 6.5 1.2 2.3z" fill="var(--green)"/></svg>
        623-555-0142
      </p>
      <p class="contact__row">
        <svg viewBox="0 0 12 12"><rect x="1" y="2.5" width="10" height="7" fill="none" stroke="var(--green)" stroke-width="1.2"/><path d="M1 2.5l5 4 5-4" fill="none" stroke="var(--green)" stroke-width="1.2"/></svg>
        hello@willowbendmortuary.example
      </p>
      <p class="contact__row">
        <svg viewBox="0 0 12 12"><circle cx="6" cy="6" r="4.8" fill="none" stroke="var(--green)" stroke-width="1.1"/><path d="M1.2 6h9.6M6 1.2c-2.5 2.6-2.5 7 0 9.6M6 1.2c2.5 2.6 2.5 7 0 9.6" fill="none" stroke="var(--green)" stroke-width="1"/></svg>
        www.willowbendmortuary.example
      </p>
    </div>
  </section>

</main>
</body>
</html>
```